House Builder and Property Development Card Design and Logo

I need a business card design for a building and property development company.
Colour scheme of Dark Grey and Green, I would like it bold, sharp and professional.
No logo yet done, I'm open to options but please stay away from the usual- house, roof, hammers etc.
Thanks Rob

Please be aware that on the business card information section the WHRC # 5528391 is a licence number and my phone number 0492837165. The numbers are close together and could be mistaken as one whole number 

Thank you

                                   

Industry/Entity Type

Building

Contact Information for Business Card

VARGA BUILD & DEVELOPMENT.
Residential Building & Property Development
Robert Varga - Director
WHRC # 5528391
0492837165
rob@vargabuild.example.com.au

Requirements
Must have
• Bold Business name
Dark grey and green colours
Should not have
• roof outline or hammer logo

```html
<!DOCTYPE html>
<html lang="en">
<head>
<meta charset="utf-8">
<title>Varga Build &amp; Development – Business Card</title>
<link rel="stylesheet" href="https://fonts.googleapis.com/css2?family=Arimo:wght@400;700&display=swap">
<style>
  :root {
    --bg: #2a2a2b;
    --card-white: #ffffff;
    --green-dark: #1d6b2c;
    --green-base: #2c8c3a;
    --green-bright: #36a246;
    --green-olive: #7ab648;
    --green-pale: #a6d17f;
    --ink: #111111;
    --grey-text: #8a8a8a;
    --font: "Arimo", Arial, sans-serif;
  }
  * { margin: 0; padding: 0; box-sizing: border-box; }
  html, body {
    width: 1200px; height: 1000px; overflow: hidden;
    background: var(--bg);
    font-family: var(--font);
  }
  .stage { position: relative; width: 1200px; height: 1000px; }

  .card {
    position: absolute; left: 250px; width: 700px; height: 400px;
    overflow: hidden; box-shadow: 0 18px 40px rgba(0,0,0,.45);
  }

  /* Back of card */
  .card-back {
    top: 60px;
    background: radial-gradient(circle at 50% 45%, var(--green-base), #1f7a30 75%);
    display: flex; flex-direction: column; align-items: center; justify-content: center;
    color: var(--card-white);
  }
  .card-back .brand-mark {
    width: 46px; height: 46px; background: var(--card-white); margin-bottom: 14px;
  }
  .card-back .brand-name { font-size: 52px; font-weight: 700; letter-spacing: .5px; line-height: 1; }
  .card-back .brand-tagline { font-size: 13px; font-weight: 700; margin-top: 8px; }

  /* Front of card */
  .card-front { top: 520px; background: var(--card-white); }
  .card-front .curves { position: absolute; inset: 0; width: 700px; height: 400px; }

  .brand-lockup {
    position: absolute; left: 40px; top: 36px;
    display: flex; align-items: center; gap: 14px;
  }
  .brand-lockup .brand-mark { width: 40px; height: 40px; background: var(--green-base); }
  .brand-lockup .brand-name { font-size: 36px; font-weight: 700; color: var(--ink); line-height: 1; }
  .brand-lockup .brand-tagline { font-size: 10px; font-weight: 700; color: var(--green-base); margin-top: 3px; }

  .person { position: absolute; left: 44px; top: 170px; }
  .person-name { font-size: 40px; font-weight: 700; color: var(--green-olive); line-height: 1; }
  .person-role { font-size: 14px; color: var(--grey-text); margin-top: 4px; }

  .contact-list { position: absolute; left: 44px; top: 270px; list-style: none; }
  .contact-item {
    display: flex; align-items: center; gap: 10px;
    font-size: 17px; color: var(--ink); line-height: 25px;
  }
  .contact-icon {
    width: 16px; height: 16px; background: var(--green-base); color: var(--card-white);
    font-size: 12px; font-weight: 700; display: inline-flex; align-items: center; justify-content: center;
  }
  .licence { font-size: 17px; font-weight: 700; color: var(--ink); margin-top: 2px; letter-spacing: .5px; }
</style>
</head>
<body>
<main class="stage">

  <section class="card card-back" aria-label="Business card back">
    <div class="brand-mark"></div>
    <div class="brand-name">Varga</div>
    <div class="brand-tagline">Residential Building &amp; Property Development</div>
  </section>

  <section class="card card-front" aria-label="Business card front">
    <svg class="curves" viewBox="0 0 700 400" aria-hidden="true">
      <defs>
        <linearGradient id="darkField" x1="0" y1="0" x2="1" y2="1">
          <stop offset="0" stop-color="#22803a"/>
          <stop offset="1" stop-color="#12502a"/>
        </linearGradient>
      </defs>
      <path d="M390,0 C480,55 590,90 700,100 L700,0 Z" fill="var(--green-pale)"/>
      <path d="M470,0 C560,45 640,65 700,68 L700,0 Z" fill="var(--green-bright)"/>
      <path d="M450,400 C480,250 570,130 700,80 L700,400 Z" fill="var(--green-olive)"/>
      <path d="M495,400 C525,265 605,160 700,118 L700,400 Z" fill="url(#darkField)"/>
    </svg>

    <div class="brand-lockup">
      <div class="brand-mark"></div>
      <div>
        <div class="brand-name">Varga</div>
        <div class="brand-tagline">Residential Building &amp; Property Development</div>
      </div>
    </div>

    <div class="person">
      <div class="person-name">Robert Varga</div>
      <div class="person-role">Director</div>
    </div>

    <ul class="contact-list">
      <li class="contact-item"><span class="contact-icon">p</span>0492 837165</li>
      <li class="contact-item"><span class="contact-icon">e</span>rob@vargabuild.example.com.au</li>
      <li class="contact-item"><span class="contact-icon">w</span>www.vargabuild.example.com.au</li>
      <li class="licence">WHRC # 5528391</li>
    </ul>
  </section>

</main>
</body>
</html>
```